Free Legal Consultation

Dean,

I am wondering if you could take the Open House invitation you created for me for KRDM and use it to create a postcard for people stopping in to let us know if they are interested in making a meeting with us.
So, front of the card - left side of the card, we would have the front door picture, then on the right side of the card,we would have the logo, underneath a picture of me,

then two locations:
742 Corbin Ave., Newton, MA
8 Tamblin Ave., Norwell, MA
(617) 438-2160.

On the back of the card, on the left side of the card 3 check boxes next to 3 categories:
Estate Planning
Estate and Trust Administration
Elder Law and Nursing Care Planning

On the right side of the card:

I am interested in a free legal consultation:

Name: ______________________________
Address: ____________________________
____________________________
Phone: ____________________________
Email: ____________________________

Can you work up a design for me?

It would be great to have it for the open house.

Thanks, Marla

```html
<!DOCTYPE html>
<html lang="en">
<head>
<meta charset="utf-8">
<title>KRDM Open House Postcard</title>
<link rel="stylesheet" href="https://fonts.googleapis.com/css2?family=Great+Vibes&family=Open+Sans:wght@400;600;700&display=swap">
<style>
  :root {
    --backdrop: #ece8e3;
    --card-dark: #2a2527;
    --card-light: #e6e6e7;
    --gold: #d2b05a;
    --muted: #9b9a9b;
    --white: #ffffff;
    --pill: #6d6e70;
    --ink: #231f20;
    --rule: #8a8a8c;
    --logo-red: #b01f2e;
    --photo-door: #7a4438;
    --photo-portrait: #6b5a63;
  }
  * { margin: 0; padding: 0; box-sizing: border-box; }
  html, body { width: 1079px; height: 1200px; overflow: hidden; }
  body {
    background: var(--backdrop);
    font-family: "Open Sans", Arial, sans-serif;
    position: relative;
  }
  .card {
    position: absolute;
    background: var(--card-dark);
    box-shadow: 0 6px 14px rgba(0,0,0,0.35);
    overflow: hidden;
  }
  .card-front { left: 75px; top: 43px; width: 832px; height: 521px; }
  .card-back { left: 153px; top: 604px; width: 833px; height: 516px; }

  .front-title {
    position: absolute; left: 69px; top: 18px;
    font-family: "Great Vibes", cursive; font-weight: 400;
    font-size: 54px; color: var(--white); line-height: 1;
  }
  .front-subtitle {
    position: absolute; left: 110px; top: 74px;
    font-size: 28px; color: var(--gold); letter-spacing: 1px;
  }
  .door-photo {
    position: absolute; left: 25px; top: 123px; width: 432px; height: 380px;
    background: linear-gradient(180deg, #8c5246 0%, var(--photo-door) 55%, #4c3a33 100%);
  }
  .firm-mark {
    position: absolute; left: 499px; top: 34px;
    display: flex; align-items: center; gap: 12px;
  }
  .firm-mark-square { width: 34px; height: 34px; background: var(--logo-red); }
  .firm-mark-name { font-size: 38px; font-weight: 600; color: var(--white); letter-spacing: 4px; line-height: 1; }
  .practice-areas {
    position: absolute; left: 499px; top: 98px; width: 320px;
    font-size: 15px; line-height: 20px; color: var(--muted);
  }
  .rsvp {
    position: absolute; left: 499px; top: 158px;
    font-size: 15px; color: var(--white);
  }
  .rsvp-email { color: var(--gold); }
  .attorney-photo {
    position: absolute; left: 586px; top: 207px; width: 133px; height: 183px;
    background: linear-gradient(180deg, #8d8a93 0%, var(--photo-portrait) 60%, #3d2c3f 100%);
  }
  .attorney-name {
    position: absolute; left: 552px; top: 394px; width: 200px; text-align: center;
    font-size: 19px; color: var(--gold);
  }
  .office-details {
    position: absolute; right: 25px; top: 445px; text-align: right;
    font-size: 15px; line-height: 18px; color: var(--muted); font-style: normal;
  }
  .office-phone { font-weight: 600; }

  .back-panel {
    position: absolute; left: 0; top: 49px; width: 100%; height: 417px;
    background: var(--card-light);
  }
  .interest-list { position: absolute; left: 43px; top: 84px; list-style: none; }
  .interest-row { display: flex; align-items: center; gap: 7px; margin-bottom: 28px; height: 65px; }
  .interest-box {
    width: 48px; height: 65px; border: 1.5px solid var(--rule); border-radius: 10px;
  }
  .interest-label {
    width: 246px; height: 65px; border-radius: 12px; background: var(--pill);
    color: var(--white); font-size: 17px; line-height: 21px; letter-spacing: -0.3px;
    text-align: center;
    display: flex; align-items: center; justify-content: center; padding: 0 4px;
  }
  .consult-form { position: absolute; left: 403px; top: 104px; width: 412px; }
  .consult-heading {
    font-size: 17px; font-weight: 700; color: var(--ink);
    letter-spacing: -0.4px; white-space: nowrap; margin-bottom: 8px;
  }
  .form-field { display: flex; align-items: flex-end; height: 42px; font-size: 15px; color: var(--ink); }
  .form-field-label { width: 62px; flex: none; }
  .form-field-label-wide { width: auto; }
  .form-field-line { flex: 1; border-bottom: 2px dotted var(--rule); height: 14px; }
</style>
</head>
<body>
  <section class="card card-front">
    <h1 class="front-title">Open House</h1>
    <p class="front-subtitle">You're Invited</p>
    <div class="door-photo" role="img" aria-label="Photo of the brick office building's front door with arched white doorway and firm sign"></div>

    <div class="firm-mark">
      <span class="firm-mark-square"></span>
      <span class="firm-mark-name">KRDM</span>
    </div>
    <p class="practice-areas">Attorneys practicing in the areas of Estate Planning, Estate and Trust Administration, Elder Law and Nursing Care Planning</p>
    <p class="rsvp">RSVP: <span class="rsvp-email">mhaskell@krdm.com</span></p>

    <div class="attorney-photo" role="img" aria-label="Portrait photo of attorney Marla Haskell"></div>
    <p class="attorney-name">Marla Haskell</p>

    <address class="office-details">
      742 Corbin Ave., Newton, MA<br>
      8 Tamblin Ave., Norwell, MA<br>
      <span class="office-phone">(617) 438-2160</span>
    </address>
  </section>

  <section class="card card-back">
    <div class="back-panel">
      <ul class="interest-list">
        <li class="interest-row"><span class="interest-box"></span><span class="interest-label">ESTATE PLANNING</span></li>
        <li class="interest-row"><span class="interest-box"></span><span class="interest-label">ESTATE AND TRUST<br>ADMINISTRATION</span></li>
        <li class="interest-row"><span class="interest-box"></span><span class="interest-label">ELDER LAW AND NURSING<br>CARE PLANNING</span></li>
      </ul>
      <div class="consult-form">
        <h2 class="consult-heading">I am interested in a free legal consultation:</h2>
        <div class="form-field"><span class="form-field-label">Name:</span><span class="form-field-line"></span></div>
        <div class="form-field"><span class="form-field-label form-field-label-wide">Address:</span><span class="form-field-line"></span></div>
        <div class="form-field"><span class="form-field-line"></span></div>
        <div class="form-field"><span class="form-field-label">Phone:</span><span class="form-field-line"></span></div>
        <div class="form-field"><span class="form-field-label">Email:</span><span class="form-field-line"></span></div>
      </div>
    </div>
  </section>
</body>
</html>
```